BrightNest - Green cleaning service blog design

We have a website, built in wordpress. We need a clean, professional and nice to read blog where we can post articles.

The blog should emphasize images/video and content/text
The blog should be easy to read and see photos
The blog should include navigation to view more articles
The blogs should have categories filters

Your blog design should have a listing page (see a listing of all articles)
Your blog design should have a detail page (full article page)
Your blog design should include responsive mobile and tablet views

You can view our site at
http://brightnest.staging.hostlark.com/

And our blog placeholder page here:
http://brightnest.staging.hostlark.com/blog/

Here are some example blog sites that I like:
https://www.plumhollowgoods.com/healthy-living
https://blog.tuliprow.com/#
http://www.dunmoss.com/blog/

Target Market(s)

mothers, parents, single professionals, enviromentalist

Industry/Entity Type

Cleaning Service

Requirements
Must have
• Reponsive Design (mobile and tablet)
• List page
• Detail page
• Use the header and footer navigation of the existing site:
• http://brightnest.staging.hostlark.com/
• There should be display for "As seen on TV" where we can show what media outlets have covered our story
• - This should live on on the blog landing page (prominently)
• - The should be a widget on the detail page
• Seet the attached image for an example of how this is used on a website (the image is not a blog, but it should give you an idea)

```html
<!DOCTYPE html>
<html lang="en">
<head>
<meta charset="utf-8">
<title>BrightNest Blog</title>
<link rel="stylesheet" href="https://fonts.googleapis.com/css2?family=Open+Sans:wght@400;600;700&family=Montserrat:wght@400;600;700&family=Oswald:wght@500&family=Bebas+Neue&display=swap">
<style>
:root{
  --navy:#071a2b;
  --white:#ffffff;
  --leaf:#8dc63f;
  --teal:#1f8a78;
  --teal-dark:#1a7466;
  --forest:#2f7a1e;
  --forest-deep:#1d4f15;
  --title-teal:#237a6b;
  --olive:#5c6b1f;
  --card-grey:#d9d9d4;
  --bar-grey:#ececec;
  --logo-grey:#6a6a6a;
  --badge-red:#e8232b;
  --next-green:#8fcf95;
  --page-grey:#8a8a8a;
  --cta-green:#7ebb34;
  --heading-green:#1f3a14;
}
*{margin:0;padding:0;box-sizing:border-box}
html,body{width:1200px;height:2853px;overflow:hidden;background:var(--white)}
body{position:relative;font-family:"Open Sans",Arial,sans-serif}
.abs{position:absolute}

/* header */
.site-header{position:absolute;left:0;top:0;width:1200px;height:87px;background:var(--navy)}
.brand{position:absolute;left:118px;top:22px;display:flex;align-items:center;gap:12px;color:var(--leaf);font-family:"Montserrat",sans-serif;font-weight:600;font-size:30px}
.brand-dot{width:40px;height:40px;border-radius:50%;background:var(--leaf)}
.main-nav{position:absolute;right:120px;top:30px;display:flex;gap:26px;font-family:"Montserrat",sans-serif;font-size:16px;color:var(--white)}
.main-nav .active{color:var(--leaf)}

/* featured */
.featured{position:absolute;left:101px;top:95px;width:1000px;height:278px;display:flex}
.feature{position:relative;flex:1;color:var(--white);padding:85px 14px 0}
.feature:nth-child(1){background:linear-gradient(160deg,#2aa08a,var(--teal-dark))}
.feature:nth-child(2){background:linear-gradient(160deg,#3f8e27,var(--forest))}
.feature:nth-child(3){background:linear-gradient(160deg,#2c6b1f,var(--forest-deep))}
.feature h2{font-size:20px;font-weight:700;margin-bottom:22px}
.feature p{font-size:14px;line-height:19px}
.feature .byline{position:absolute;left:10px;bottom:10px;font-size:13px;font-weight:600}
.feature .share{position:absolute;right:10px;bottom:12px;display:flex;gap:6px}
.share span{width:11px;height:11px;border-radius:50%;background:var(--white)}

/* press */
.press{position:absolute;left:101px;top:403px;width:1000px;height:99px;background:var(--bar-grey)}
.tv-badge{position:absolute;left:110px;top:386px;width:80px;height:61px;border-radius:8px;background:var(--badge-red)}
.outlet{position:absolute;top:440px;font-family:"Open Sans",sans-serif;font-weight:700;font-size:25px;color:var(--logo-grey)}

/* posts */
.post{position:absolute;left:101px;width:998px;height:366px;display:flex}
.post-text{width:397px;height:100%;background:radial-gradient(ellipse at 40% 45%,#e6e6e2,var(--card-grey));padding:58px 16px 0 15px}
.post-text h3{font-weight:400;font-size:30px;line-height:37px;color:var(--title-teal);margin-bottom:8px}
.post-text p{font-size:14.5px;line-height:19px;color:var(--olive);text-align:justify}
.post-text .read-more{display:block;margin-top:14px;font-size:20px;color:var(--olive)}
.post-photo{flex:1;height:100%;background:linear-gradient(100deg,#2b2a1e 0%,#5b6448 30%,#9aa27e 55%,#3f5a2a 75%,#1f2a15 100%)}

/* popular */
.popular-title{position:absolute;left:100px;top:2022px;font-family:"Bebas Neue",sans-serif;font-size:42px;color:var(--heading-green)}
.pop-card{position:absolute;top:2071px;width:327px;height:249px}
.pop-photo{height:160px;background:linear-gradient(180deg,#cfd8cf 0%,#6e9a5a 45%,#3f6f2e 100%)}
.pop-caption{height:89px;background:var(--teal);color:var(--white);font-family:"Oswald",sans-serif;font-weight:500;font-size:26px;padding:22px 0 0 10px;white-space:nowrap}

/* pager */
.next-btn{position:absolute;left:525px;top:2353px;width:152px;height:59px;background:var(--next-green);color:var(--white);font-family:"Montserrat",sans-serif;font-size:26px;display:flex;align-items:center;justify-content:center;box-shadow:0 2px 3px rgba(0,0,0,.25)}
.pager{position:absolute;left:814px;top:2366px;display:flex;align-items:center;gap:8px;font-family:"Oswald",sans-serif;font-size:24px;color:var(--page-grey)}
.pager .current{border:1px solid #bbb;width:40px;height:36px;display:flex;align-items:center;justify-content:center}

/* footer */
.site-footer{position:absolute;left:0;top:2448px;width:1200px;height:405px;background:var(--navy);color:var(--white);font-family:"Montserrat",sans-serif}
.site-footer .t{position:absolute;font-size:14px;white-space:nowrap}
.site-footer .h{font-weight:700;font-size:17px}
.site-footer .b{font-weight:700}
.social{position:absolute;width:28px;height:28px;border-radius:50%;background:var(--white)}
.schedule-btn{position:absolute;left:782px;top:101px;width:158px;height:38px;border-radius:5px;background:var(--cta-green);font-weight:700;font-size:14px;display:flex;align-items:center;justify-content:center}
.mailing-btn{position:absolute;left:782px;top:291px;width:194px;height:47px;border:2px solid var(--cta-green);border-radius:6px;font-weight:700;font-size:14px;display:flex;align-items:center;justify-content:center}
</style>
</head>
<body>

<header class="site-header">
  <div class="brand"><span class="brand-dot"></span>brightnest</div>
  <nav class="main-nav"><span>home</span><span>services</span><span>about</span><span>going green</span><span class="active">blog</span><span>contact</span></nav>
</header>

<section class="featured">
  <article class="feature" role="img" aria-label="Featured post over a green interior photo">
    <h2>Ut wisi enim ad minim veniam</h2>
    <p>Ut wisi enim ad minim veniam, quis nostrud exerci tation ullamcorper suscipit lobortis nisl ut aliquip ex ea commodo consequat.</p>
    <div class="byline">By: Rowan &nbsp;&nbsp; 21 Hrs ago</div>
    <div class="share"><span></span><span></span><span></span></div>
  </article>
  <article class="feature" role="img" aria-label="Featured post over a leafy plant photo">
    <h2>Ut wisi enim ad minim veniam</h2>
    <p>Ut wisi enim ad minim veniam, quis nostrud exerci tation ullamcorper suscipit lobortis nisl ut aliquip ex ea commodo consequat.</p>
    <div class="byline">By: Rowan &nbsp;&nbsp; 21 Hrs ago</div>
    <div class="share"><span></span><span></span><span></span></div>
  </article>
  <article class="feature" role="img" aria-label="Featured post over a conservatory photo">
    <h2>Ut wisi enim ad minim veniam</h2>
    <p>Ut wisi enim ad minim veniam, quis nostrud exerci tation ullamcorper suscipit lobortis nisl ut aliquip ex ea commodo consequat.</p>
    <div class="byline">By: Rowan &nbsp;&nbsp; 21 Hrs ago</div>
    <div class="share"><span></span><span></span><span></span></div>
  </article>
</section>

<section aria-label="As seen on TV">
  <div class="press"></div>
  <div class="tv-badge" aria-hidden="true"></div>
  <span class="outlet" style="left:210px">The Daily Ledger</span>
  <span class="outlet" style="left:490px">ByteWire</span>
  <span class="outlet" style="left:776px">MKTV</span>
  <span class="outlet" style="left:912px">Stockwell</span>
</section>

<main>
  <article class="post" style="top:515px">
    <div class="post-text">
      <h3>Duis autem vel eum iriure dolor in hendrerit</h3>
      <p>Lorem ipsum dolor sit amet, consectetuer adipiscing elit, sed diam nonummy nibh euismod tincidunt ut laoreet dolore magna aliquam erat volutpat. Ut wisi enim ad minim veniam, quis nostrud exerci tation ullamcorper suscipit lobortis nisl ut aliquip ex ea commodo consequat. Duis autem vel eum iriure dolor in hendrerit in vulputate velit esse molestie consequat, vel illum dolore eu feugiat nulla facilisis at vero eros et accumsan et.</p>
      <span class="read-more">Read More</span>
    </div>
    <div class="post-photo" role="img" aria-label="Sunlit café room filled with large potted plants"></div>
  </article>
  <article class="post" style="top:894px">
    <div class="post-text">
      <h3>Duis autem vel eum iriure dolor in hendrerit</h3>
      <p>Lorem ipsum dolor sit amet, consectetuer adipiscing elit, sed diam nonummy nibh euismod tincidunt ut laoreet dolore magna aliquam erat volutpat. Ut wisi enim ad minim veniam, quis nostrud exerci tation ullamcorper suscipit lobortis nisl ut aliquip ex ea commodo consequat. Duis autem vel eum iriure dolor in hendrerit in vulputate velit esse molestie consequat, vel illum dolore eu feugiat nulla facilisis at vero eros et accumsan et.</p>
      <span class="read-more">Read More</span>
    </div>
    <div class="post-photo" role="img" aria-label="Sunlit café room filled with large potted plants"></div>
  </article>
  <article class="post" style="top:1272px">
    <div class="post-text">
      <h3>Duis autem vel eum iriure dolor in hendrerit</h3>
      <p>Lorem ipsum dolor sit amet, consectetuer adipiscing elit, sed diam nonummy nibh euismod tincidunt ut laoreet dolore magna aliquam erat volutpat. Ut wisi enim ad minim veniam, quis nostrud exerci tation ullamcorper suscipit lobortis nisl ut aliquip ex ea commodo consequat. Duis autem vel eum iriure dolor in hendrerit in vulputate velit esse molestie consequat, vel illum dolore eu feugiat nulla facilisis at vero eros et accumsan et.</p>
      <span class="read-more">Read More</span>
    </div>
    <div class="post-photo" role="img" aria-label="Sunlit café room filled with large potted plants"></div>
  </article>
  <article class="post" style="top:1651px">
    <div class="post-text">
      <h3>Duis autem vel eum iriure dolor in hendrerit</h3>
      <p>Lorem ipsum dolor sit amet, consectetuer adipiscing elit, sed diam nonummy nibh euismod tincidunt ut laoreet dolore magna aliquam erat volutpat. Ut wisi enim ad minim veniam, quis nostrud exerci tation ullamcorper suscipit lobortis nisl ut aliquip ex ea commodo consequat. Duis autem vel eum iriure dolor in hendrerit in vulputate velit esse molestie consequat, vel illum dolore eu feugiat nulla facilisis at vero eros et accumsan et.</p>
      <span class="read-more">Read More</span>
    </div>
    <div class="post-photo" role="img" aria-label="Sunlit café room filled with large potted plants"></div>
  </article>
</main>

<section aria-label="Popular posts">
  <h2 class="popular-title">POPULAR POST</h2>
  <article class="pop-card" style="left:103px">
    <div class="pop-photo" role="img" aria-label="Greenhouse full of flowering plants"></div>
    <div class="pop-caption">[1] Lorem ipsum dolor sit amet</div>
  </article>
  <article class="pop-card" style="left:439px">
    <div class="pop-photo" role="img" aria-label="Greenhouse full of flowering plants"></div>
    <div class="pop-caption">[1] Lorem ipsum dolor sit amet</div>
  </article>
  <article class="pop-card" style="left:774px">
    <div class="pop-photo" role="img" aria-label="Greenhouse full of flowering plants"></div>
    <div class="pop-caption">[1] Lorem ipsum dolor sit amet</div>
  </article>
</section>

<nav aria-label="Pagination">
  <div class="next-btn">NEXT</div>
  <div class="pager"><span>Page</span><span class="current">1</span><span>150</span></div>
</nav>

<footer class="site-footer">
  <span class="t h" style="left:143px;top:48px">brightnest</span>
  <svg class="abs" style="left:143px;top:86px" width="18" height="18" viewBox="0 0 24 24"><path fill="#fff" d="M6.6 10.8a15 15 0 0 0 6.6 6.6l2.2-2.2c.3-.3.7-.4 1-.2 1.1.4 2.3.6 3.6.6.6 0 1 .4 1 1V20c0 .6-.4 1-1 1A17 17 0 0 1 3 4c0-.6.4-1 1-1h3.5c.6 0 1 .4 1 1 0 1.3.2 2.5.6 3.6.1.3 0 .7-.2 1z"/></svg>
  <span class="t b" style="left:173px;top:85px;font-size:16px">1.800.555.0142</span>
  <span class="t" style="left:173px;top:122px">Mon–Fri: 9am–6pm</span>
  <span class="t" style="left:173px;top:145px">Sat–Sun: 9am–3pm</span>
  <svg class="abs" style="left:143px;top:200px" width="18" height="24" viewBox="0 0 18 24"><path fill="#fff" d="M9 0a9 9 0 0 0-9 9c0 6.5 9 15 9 15s9-8.5 9-15a9 9 0 0 0-9-9zm0 12.5A3.5 3.5 0 1 1 9 5.5a3.5 3.5 0 0 1 0 7z"/></svg>
  <span class="t" style="left:173px;top:202px">18 Alder Court, 4th Floor,</span>
  <span class="t" style="left:173px;top:225px">#4120</span>
  <span class="t" style="left:173px;top:250px">Fairhaven, NY 10099</span>
  <span class="social" style="left:174px;top:307px"></span>
  <span class="social" style="left:220px;top:307px"></span>
  <span class="social" style="left:266px;top:307px"></span>

  <span class="t h" style="left:477px;top:48px">company</span>
  <span class="t" style="left:477px;top:89px">about</span>
  <span class="t" style="left:477px;top:114px">contact</span>
  <span class="t" style="left:477px;top:139px">careers</span>
  <span class="t h" style="left:477px;top:175px">what we do</span>
  <span class="t" style="left:477px;top:222px">services</span>
  <span class="t" style="left:477px;top:247px">going green</span>
  <span class="t" style="left:477px;top:272px">blog</span>

  <span class="t h" style="left:782px;top:48px">book online now!</span>
  <div class="schedule-btn">schedule now</div>
  <span class="t b" style="left:782px;top:165px;font-size:13px">join the brightnest mailing lists</span>
  <span class="t b" style="left:782px;top:188px;font-size:13px">today</span>
  <span class="t" style="left:782px;top:224px;font-size:12px">Signup today to receive promotions,</span>
  <span class="t" style="left:782px;top:247px;font-size:12px">discounts, and updates.</span>
  <div class="mailing-btn">join our mailing list</div>

  <span class="t" style="left:556px;top:384px;font-size:12px">© brightnest</span>
</footer>

</body>
</html>
```